Football and Sports Management Agency Stationary

We have a logo, fonts, website and colour palette.
We need the logo refined by a proper designer and then business stationary designed. You can see on the website how it needs adjusting by a designers eye.
The company is a high end sports management company aiming to attract and represent professional athletes. The name Veltor is to indicate a 'Constellation of Stars' ie our clients. The dots on the star should be slightly different sizes to reflect that some clients will be bigger than others.
Colours:
#e6e6e6
#edd2a4
#caaa72 (main gold and also used on site)
#3f3f42
#001d38
#edeced (on website)
#191c23 (on website)
Font:
LS (veltor)
SF Florencesans (sports management)
We would like:
- Letterhead (word and indesign and PDF print format). I have attached an example for one I like. It's quiet a clean design with the contact details and address taking up only a small amount of room.
- Business card (dark on the back with the logo, personal details on the front). Only needs name, title, email, website and phone number. No company address (in PDF and indesign format)
- Powerpoint slide theme
- Logo in vector format for light and dark versions and single colour versions. And optimised web version
- Simple brand guide PDF showing colour, font and logo (a one/two page PDF)
Any questions, please ask.
NEW INFO:
Contact Details
Maren Odsworth
Director
Mobile: +44 7312 908 271
Phone: +44 0113 872 604
Email: maren@veltorathletic-example.com
Web: veltorathletic-example.com
Bramwell Court, 14 Orchard Rise, Hazel Grove, Stockport, SK9 2QT
Company number 20948367
Target Market(s)
Professional athletes, professional sports teams.
Industry/Entity Type
Management
Requirements
Must have
- NEW
- The designs must look cool, classy and high quality. My suggestion for this is to keep the text small and precise with uncomplicated design.
Nice to have
- Application of brand displayed on stationary and additional pieces of stationary branded.
- Draw some inspiration from the website. eg the slant angles used separate the sections.
Should not have
- Don't create new logos etc.

```html
<!DOCTYPE html>
<html lang="en">
<head>
<meta charset="utf-8">
<title>Veltor Sports Management – Stationery &amp; Brand Board</title>
<link href="https://fonts.googleapis.com/css2?family=Open+Sans:ital,wght@0,300;0,400;0,600;0,700;1,600&display=swap" rel="stylesheet">
<style>
  :root{
    --board:#e4e4e4;
    --paper:#ffffff;
    --gold:#caaa72;
    --gold-soft:#edd2a4;
    --grey-light:#e6e6e6;
    --grey-light-2:#edeced;
    --grey-dark:#3f3f42;
    --ink-dark:#191c23;
    --navy:#001d38;
    --text:#2b2b2e;
    --muted:#6d6d72;
  }
  *{box-sizing:border-box;margin:0;padding:0}
  html,body{width:1200px;height:1200px;overflow:hidden;background:var(--board)}
  body{font-family:"Open Sans",Arial,sans-serif;color:var(--text)}
  .board{position:relative;width:1200px;height:1200px;overflow:hidden}
  .abs{position:absolute}

  /* brand name lockup */
  .mark{display:inline-flex;align-items:center;gap:.45em;font-family:"Open Sans",Arial,sans-serif;font-weight:300;letter-spacing:.42em;color:var(--grey-dark);white-space:nowrap}
  .mark__dot{width:.55em;height:.55em;border-radius:50%;background:var(--gold);flex:none}
  .mark--light{color:#fff}
  .mark--stack{flex-direction:column;gap:.35em}

  .hero-lockup{position:absolute;left:496px;top:62px;width:215px;display:flex;align-items:center;gap:12px}
  .hero-lockup__dot{width:14px;height:14px;border-radius:50%;background:var(--gold);flex:none}
  .hero-lockup__words{display:flex;flex-direction:column;align-items:flex-start}
  .hero-lockup__name{font-weight:300;font-size:26px;letter-spacing:.42em;line-height:1;color:var(--grey-dark)}
  .hero-lockup__sub{margin-top:5px;padding-left:14px;font-size:6.5px;letter-spacing:.5em;color:var(--grey-dark);white-space:nowrap}

  .section-title{position:absolute;left:34px;font-style:italic;font-weight:600;font-size:13px;letter-spacing:.16em;color:#1d1d20}

  .shadow{box-shadow:0 1px 4px rgba(0,0,0,.14)}

  /* letterhead */
  .letter{position:absolute;top:149px;width:266px;height:373px;background:var(--paper)}
  .letter .mark{position:absolute;left:24px;top:34px;font-size:9px}
  .letter__to{position:absolute;left:35px;top:110px;font-size:3.6px;line-height:1.5}
  .letter__to b{font-weight:700;font-size:4.2px}
  .letter__date{margin-top:6px}
  .letter__body{position:absolute;left:35px;top:172px;width:199px;font-size:3.6px;line-height:1.6;color:#333}
  .letter__body p{margin-bottom:5px}
  .letter__sign{position:absolute;left:35px;top:254px}
  .letter__signoff{position:absolute;left:35px;top:270px;font-size:3.6px;line-height:1.5}
  .letter__signoff b{font-size:4px;font-weight:700}
  .letter__foot{position:absolute;left:24px;top:322px;display:flex;gap:14px}
  .foot-item{width:46px;text-align:center;font-size:3px;line-height:1.5;color:#555}
  .foot-item svg{display:block;margin:0 auto 4px}
  .foot-item::after{content:"";display:block;width:10px;height:1px;background:var(--gold);margin:4px auto 0}

  /* business cards */
  .card{position:absolute;left:612px;width:131px;height:84px;background:var(--grey-dark);color:#fff}
  .card--back{top:322px;display:flex;align-items:center;justify-content:center}
  .card--back .mark{font-size:8px}
  .card--front{top:437px;text-align:center}
  .card__dot{width:5px;height:5px;border-radius:50%;background:var(--gold);margin:14px auto 8px}
  .card__name{font-size:5px;font-weight:600}
  .card__role{font-size:3.6px;color:var(--gold);margin-top:1px}
  .card__row{display:flex;justify-content:center;gap:10px;margin-top:10px;font-size:3.6px;color:var(--gold-soft)}
  .card__row span{display:inline-flex;align-items:center;gap:2px}
  .card__mail{font-size:3.6px;color:var(--gold-soft);margin-top:7px}

  /* slides */
  .slide{position:absolute;width:266px;height:149px;background:var(--ink-dark);overflow:hidden;color:#fff}
  .slide__photo{position:absolute}
  .slide__title{position:absolute;font-weight:700;letter-spacing:.2em;font-size:10px;line-height:1.15}
  .slide__small{position:absolute;font-size:3.2px;line-height:1.55;color:#cfd0d4}
  .photo-stadium{background:radial-gradient(ellipse at 50% 70%,#3e5a2c 0%,#24311f 30%,#1a2130 60%,#10141c 100%)}
  .photo-pitch{background:linear-gradient(180deg,#3d4650 0%,#59646b 30%,#3f6a2f 55%,#4d8a35 100%)}
  .photo-players{background:linear-gradient(180deg,#6c6f6f 0%,#8a8d8c 45%,#c9c9c5 70%,#505a40 100%)}
  .photo-strike{background:linear-gradient(180deg,#234e73 0%,#2e6fa0 30%,#3d7a2c 55%,#5d9a3d 100%)}
  .photo-portrait{background:linear-gradient(160deg,#3a1c14 0%,#1d2333 55%,#0f1422 100%)}
  .photo-mono{background:linear-gradient(120deg,#d9d9d9 0%,#8e8e8e 45%,#3d3d3d 100%)}

  /* brand guide pages */
  .page{position:absolute;top:968px;width:266px;height:188px;background:var(--paper);overflow:hidden}
  .page__head{position:relative;height:21px;font-size:4.6px}
  .page__head::before{content:"";position:absolute;inset:0;background:var(--ink-dark);clip-path:polygon(0 0,100% 0,100% 100%,59% 100%,51% 0,0 0,0 8%,0 0)}
  .page__head::after{content:"";position:absolute;left:0;top:0;width:100%;height:2px;background:var(--ink-dark)}
  .page__brand{position:absolute;left:10px;top:8px;color:var(--ink-dark)}
  .page__brand b{font-weight:700}
  .page__doc{position:absolute;right:9px;top:8px;color:#fff}
  .page__label{position:absolute;left:9px;font-size:4.6px;font-weight:700;color:var(--ink-dark)}
  .page__num{position:absolute;right:9px;bottom:8px;font-size:3.4px;color:#555}
  .tiny{font-size:3.4px;line-height:1.55;color:#444}
  .swatch-row{position:absolute;display:flex;align-items:center;gap:6px}
  .swatch{width:11px;height:11px;flex:none}
  .swatch-meta{width:32px}
  .guide-list{list-style:disc;padding-left:6px}
  .alpha{font-size:4.4px;letter-spacing:.22em;line-height:1.6;color:#333}
  .font-name{font-size:6.4px;color:#222;margin-bottom:3px}
  .icon-cap{position:absolute;text-align:center;width:40px;font-size:3.2px;color:#555}
  .icon-cap svg{display:block;margin:0 auto 3px}
</style>
</head>
<body>
<main class="board">

  <!-- top brand line -->
  <div class="hero-lockup">
    <i class="hero-lockup__dot"></i>
    <div class="hero-lockup__words">
      <span class="hero-lockup__name">VELTOR</span>
      <span class="hero-lockup__sub">SPORTS MANAGEMENT</span>
    </div>
  </div>

  <h2 class="section-title" style="top:116px;">Letterhead/ name card</h2>

  <!-- letterheads -->
  <section class="letter shadow" style="left:34px;">
    <span class="mark"><i class="mark__dot"></i><span>VELTOR</span></span>
    <div class="letter__to">To<br><b>Maren Odsworth</b><br>Director<div class="letter__date">2018 May 6</div></div>
    <div class="letter__body">
      <p>Thank you for meeting with our team last week. We are pleased to confirm the next steps for representation and will share the full outline shortly.</p>
      <p>Our agency works closely with each athlete on contracts, sponsorship and long term career planning. Every client receives a dedicated manager and a clear plan for the season ahead.</p>
      <p>Please review the enclosed summary and let us know a suitable time to talk through the details together.</p>
      <p>We look forward to working with you.</p>
    </div>
    <svg class="letter__sign" width="40" height="12" viewBox="0 0 40 12"><path d="M2 9 Q8 1 12 7 T22 6 L38 5" fill="none" stroke="#222" stroke-width=".6"/></svg>
    <div class="letter__signoff"><b>James Doe</b><br>Manager</div>
    <div class="letter__foot">
      <div class="foot-item">
        <svg width="6" height="6" viewBox="0 0 10 10"><circle cx="5" cy="5" r="4.5" fill="none" stroke="#333" stroke-width=".7"/><path d="M3.5 3 L4.5 3 L5 4.3 L4.4 4.8 Q5 6 5.8 6.4 L6.3 5.8 L7.4 6.3 L7.2 7.2 Q4 7.3 3.2 3.6Z" fill="#333"/></svg>
        +44 7312 908 271<br>+44 0113 872 604
      </div>
      <div class="foot-item">
        <svg width="6" height="6" viewBox="0 0 10 10"><circle cx="5" cy="5" r="4.5" fill="none" stroke="#333" stroke-width=".7"/><circle cx="5" cy="5" r="2.2" fill="none" stroke="#333" stroke-width=".6"/><path d="M2.8 5 H7.2 M5 2.8 V7.2" stroke="#333" stroke-width=".5"/></svg>
        veltorathletic-example.com
      </div>
      <div class="foot-item">
        <svg width="6" height="6" viewBox="0 0 10 10"><circle cx="5" cy="5" r="4.5" fill="none" stroke="#333" stroke-width=".7"/><path d="M5 2.4 A1.8 1.8 0 0 1 6.8 4.2 Q6.8 5.4 5 7.6 Q3.2 5.4 3.2 4.2 A1.8 1.8 0 0 1 5 2.4Z" fill="#333"/></svg>
        14 Orchard Rise, Ashvale,<br>Marlbury, SK9 2QT
      </div>
    </div>
  </section>

  <section class="letter shadow" style="left:323px;">
    <span class="mark"><i class="mark__dot"></i><span>VELTOR</span></span>
    <div class="letter__to">To<br><b>Maren Odsworth</b><br>Director<div class="letter__date">2018 May 6</div></div>
    <div class="letter__body">
      <p>Thank you for meeting with our team last week. We are pleased to confirm the next steps for representation and will share the full outline shortly.</p>
      <p>Our agency works closely with each athlete on contracts, sponsorship and long term career planning. Every client receives a dedicated manager and a clear plan for the season ahead.</p>
      <p>Please review the enclosed summary and let us know a suitable time to talk through the details together.</p>
      <p>We look forward to working with you.</p>
    </div>
    <svg class="letter__sign" width="40" height="12" viewBox="0 0 40 12"><path d="M2 9 Q8 1 12 7 T22 6 L38 5" fill="none" stroke="#222" stroke-width=".6"/></svg>
    <div class="letter__signoff"><b>James Doe</b><br>Manager</div>
    <div class="letter__foot">
      <div class="foot-item">
        <svg width="6" height="6" viewBox="0 0 10 10"><circle cx="5" cy="5" r="4.5" fill="none" stroke="#333" stroke-width=".7"/><path d="M3.5 3 L4.5 3 L5 4.3 L4.4 4.8 Q5 6 5.8 6.4 L6.3 5.8 L7.4 6.3 L7.2 7.2 Q4 7.3 3.2 3.6Z" fill="#333"/></svg>
        +44 7312 908 271<br>+44 0113 872 604
      </div>
      <div class="foot-item">
        <svg width="6" height="6" viewBox="0 0 10 10"><circle cx="5" cy="5" r="4.5" fill="none" stroke="#333" stroke-width=".7"/><circle cx="5" cy="5" r="2.2" fill="none" stroke="#333" stroke-width=".6"/><path d="M2.8 5 H7.2 M5 2.8 V7.2" stroke="#333" stroke-width=".5"/></svg>
        veltorathletic-example.com
      </div>
      <div class="foot-item">
        <svg width="6" height="6" viewBox="0 0 10 10"><circle cx="5" cy="5" r="4.5" fill="none" stroke="#333" stroke-width=".7"/><path d="M5 2.4 A1.8 1.8 0 0 1 6.8 4.2 Q6.8 5.4 5 7.6 Q3.2 5.4 3.2 4.2 A1.8 1.8 0 0 1 5 2.4Z" fill="#333"/></svg>
        14 Orchard Rise, Ashvale,<br>Marlbury, SK9 2QT
      </div>
    </div>
  </section>

  <!-- business cards -->
  <section class="card card--back shadow">
    <span class="mark mark--light mark--stack"><i class="mark__dot"></i><span>VELTOR</span></span>
  </section>
  <section class="card card--front shadow">
    <div class="card__dot"></div>
    <div class="card__name">Maren Odsworth</div>
    <div class="card__role">Director</div>
    <div class="card__row">
      <span>+44 0113 872 604</span>
      <span>veltorathletic-example.com</span>
    </div>
    <div class="card__mail">maren@veltorathletic-example.com</div>
  </section>

  <h2 class="section-title" style="top:553px;">Slide theme</h2>

  <!-- slides row 1 -->
  <section class="slide shadow" style="left:34px;top:586px;">
    <div class="slide__photo photo-stadium" role="img" aria-label="Dimmed night view of a floodlit football stadium" style="inset:0;"></div>
    <div class="abs" style="left:0;right:0;top:66px;text-align:center;">
      <span class="mark mark--light" style="font-size:10px;"><i class="mark__dot"></i><span>VELTOR</span></span>
    </div>
    <p class="slide__small" style="left:60px;right:60px;bottom:12px;text-align:center;">A quiet team behind the athletes who lead the game, on and off the pitch.</p>
  </section>

  <section class="slide shadow" style="left:323px;top:586px;">
    <div class="slide__photo photo-players" role="img" aria-label="Football team celebrating a goal together on the pitch" style="inset:0;"></div>
    <div class="abs" style="inset:0;background:var(--ink-dark);clip-path:polygon(0 62%,100% 40%,100% 100%,0 100%);"></div>
    <h3 class="slide__title" style="left:17px;top:110px;font-size:8px;">SPORT MANAGER</h3>
    <p class="slide__small" style="left:17px;top:123px;width:170px;">We guide professional careers with care, from first contract to final whistle, with a network built on trust and results.</p>
  </section>

  <section class="slide shadow" style="left:612px;top:586px;">
    <div class="slide__photo photo-strike" role="img" aria-label="Player striking a football on a green pitch" style="inset:0;clip-path:polygon(0 44%,100% 56%,100% 100%,0 100%);"></div>
    <h3 class="slide__title" style="left:42px;top:37px;">SPORT</h3>
    <p class="slide__small" style="left:142px;top:24px;width:105px;font-weight:700;color:#fff;font-size:3.4px;">Representation built for the modern athlete.</p>
    <p class="slide__small" style="left:142px;top:38px;width:105px;">Contract talks, brand partnerships and career planning handled by a small team with deep experience across European football.</p>
  </section>

  <!-- slides row 2 -->
  <section class="slide shadow" style="left:34px;top:755px;">
    <div class="slide__photo photo-portrait" role="img" aria-label="Portrait of a football player in a dark club kit" style="left:163px;top:0;right:0;bottom:0;"></div>
    <p class="slide__small" style="left:15px;top:52px;">Demo text</p>
    <h3 class="slide__title" style="left:15px;top:59px;">SPORT MANAGER</h3>
    <p class="abs" style="left:15px;top:74px;font-size:6.4px;font-weight:700;color:var(--gold);letter-spacing:.06em;">Daniel Harcourt</p>
  </section>

  <section class="slide shadow" style="left:323px;top:755px;">
    <div class="slide__photo photo-pitch" role="img" aria-label="Wide view of a packed football stadium and pitch" style="left:0;top:0;width:165px;bottom:0;"></div>
    <h3 class="slide__title" style="left:178px;top:33px;font-size:8px;">SPORT<br>MANAGER</h3>
    <ul class="slide__small" style="left:182px;top:58px;width:74px;list-style:disc;line-height:3.3;">
      <li>Contract negotiation</li>
      <li>Sponsorship and brand deals</li>
      <li>Career and transfer planning</li>
      <li>Media and public relations</li>
      <li>Financial guidance</li>
      <li>Aftercare and transition</li>
    </ul>
  </section>

  <section class="slide shadow" style="left:612px;top:755px;">
    <div class="slide__photo photo-mono" role="img" aria-label="Black and white portrait of a player holding a ball" style="left:0;top:0;width:133px;bottom:0;"></div>
    <h3 class="slide__title" style="left:146px;top:33px;font-size:8.5px;">TOMAS REYVAL</h3>
    <p class="slide__small" style="left:146px;top:51px;width:106px;font-weight:700;color:#fff;font-size:3.6px;">A season in focus</p>
    <p class="slide__small" style="left:146px;top:57px;width:106px;text-align:justify;">A forward known for vision and calm under pressure, he joined the agency early in his career. Together we have shaped transfers, endorsements and a lasting public profile built on steady performance.</p>
  </section>

  <h2 class="section-title" style="top:931px;">Simple brand guide</h2>

  <!-- brand guide: logo -->
  <section class="page shadow" style="left:34px;">
    <header class="page__head"><span class="page__brand"><b>VELTOR</b> SPORTS MANAGEMENT</span><span class="page__doc">Brand Guideline</span></header>
    <span class="page__label" style="top:27px;">LOGO</span>
    <div class="abs" style="left:0;right:0;top:52px;text-align:center;">
      <span class="mark mark--stack" style="font-size:12px;"><i class="mark__dot"></i><span>VELTOR</span></span>
    </div>
    <span class="page__label" style="top:116px;">LOGO VARIATIONS</span>
    <div class="abs tiny" style="left:30px;top:140px;text-align:center;">
      <span class="mark" style="font-size:6px;"><i class="mark__dot"></i><span>VELTOR</span></span>
      <div style="margin-top:12px;">Horizontal logo - color</div>
    </div>
    <div class="abs tiny" style="left:120px;top:133px;text-align:center;">
      <span class="mark mark--stack" style="font-size:6px;"><i class="mark__dot"></i><span>VELTOR</span></span>
      <div style="margin-top:9px;">Vertical logo - color</div>
    </div>
    <div class="abs tiny" style="left:212px;top:140px;text-align:center;">
      <i class="mark__dot" style="display:block;width:6px;height:6px;border-radius:50%;background:var(--gold);margin:0 auto;"></i>
      <div style="margin-top:12px;">Icon - color</div>
    </div>
    <span class="page__num">Page I</span>
  </section>

  <!-- brand guide: colour -->
  <section class="page shadow" style="left:323px;">
    <header class="page__head"><span class="page__brand"><b>VELTOR</b> SPORTS MANAGEMENT</span><span class="page__doc">Brand Guideline</span></header>
    <span class="page__label" style="top:27px;">COLOR</span>
    <span class="abs tiny" style="left:17px;top:47px;">Primary color</span>
    <div class="swatch-row tiny" style="left:58px;top:44px;"><i class="swatch" style="background:var(--gold)"></i><span class="swatch-meta">Gold<br>Hex: #caaa72</span><span>RGB: 202/170/114<br>CMYK: 22/31/63/0</span></div>
    <span class="abs tiny" style="left:17px;top:76px;">Secondary colors</span>
    <div class="swatch-row tiny" style="left:58px;top:72px;"><i class="swatch" style="background:var(--grey-light)"></i><span class="swatch-meta">Light Grey<br>Hex: #e6e6e6</span><span>RGB: 230/230/230<br>CMYK: 8/6/7/0</span></div>
    <div class="swatch-row tiny" style="left:58px;top:89px;"><i class="swatch" style="background:var(--grey-dark)"></i><span class="swatch-meta">Dark Grey<br>Hex: #3f3f42</span><span>RGB: 63/63/66<br>CMYK: 69/62/58/46</span></div>
    <div class="swatch-row tiny" style="left:58px;top:106px;"><i class="swatch" style="background:var(--navy)"></i><span class="swatch-meta">Navy<br>Hex: #001d38</span><span>RGB: 0/29/56<br>CMYK: 97/81/47/60</span></div>
    <div class="swatch-row tiny" style="left:160px;top:72px;"><i class="swatch" style="background:var(--grey-light-2)"></i><span class="swatch-meta">Light Grey 2<br>Hex: #edeced</span><span>RGB: 237/236/237<br>CMYK: 6/5/4/0</span></div>
    <div class="swatch-row tiny" style="left:160px;top:89px;"><i class="swatch" style="background:var(--ink-dark)"></i><span class="swatch-meta">Dark Grey 2<br>Hex: #191c23</span><span>RGB: 25/28/35<br>CMYK: 78/70/59/74</span></div>
    <div class="abs tiny" style="left:17px;top:128px;width:230px;">
      <p style="margin-bottom:4px;">This is how we use the color scheme:</p>
      <ul class="guide-list">
        <li>Gold is the main color and is also used on site</li>
        <li>Light Grey, Dark Grey and Navy are used when needed</li>
        <li>Light Grey 2 and Dark Grey 2 are used on the website</li>
        <li>Light Grey keeps the look light, simple and clean</li>
      </ul>
    </div>
    <span class="page__num">Page II</span>
  </section>

  <!-- brand guide: font -->
  <section class="page shadow" style="left:612px;">
    <header class="page__head"><span class="page__brand"><b>VELTOR</b> SPORTS MANAGEMENT</span><span class="page__doc">Brand Guideline</span></header>
    <span class="page__label" style="top:27px;">FONT</span>
    <ul class="abs tiny guide-list" style="left:22px;top:38px;width:220px;">
      <li>LS used for the word VELTOR</li>
      <li>SF Florencesans used for SPORTS MANAGEMENT</li>
      <li>Open Sans is the supplementary font for online text</li>
    </ul>
    <span class="abs tiny" style="left:18px;top:72px;">Primary font</span>
    <span class="abs tiny" style="left:148px;top:72px;">Supplementary font</span>
    <div class="abs" style="left:18px;right:10px;top:79px;height:.5px;background:#999;"></div>
    <div class="abs" style="left:18px;top:96px;">
      <div class="font-name">LS</div>
      <div class="alpha">ABCDEFGHIJKLMNOPQRSTUVWXYZ<br>abcdefghijklmnopqrstuvwxyz<br>0123456789</div>
    </div>
    <div class="abs" style="left:148px;top:96px;">
      <div class="font-name">Open Sans</div>
      <div class="alpha">ABCDEFGHIJKLMNOPQRSTUVWXYZ<br>abcdefghijklmnopqrstuvwxyz<br>0123456789</div>
    </div>
    <div class="abs" style="left:18px;top:140px;">
      <div class="font-name">SF Florencesans</div>
      <div class="alpha" style="font-size:3.6px;">ABCDEFGHIJKLMNOPQRSTUVWXYZ<br>abcdefghijklmnopqrstuvwxyz<br>0123456789</div>
    </div>
    <span class="page__num">Page III</span>
  </section>

  <!-- brand guide: icons -->
  <section class="page shadow" style="left:901px;">
    <header class="page__head"><span class="page__brand"><b>VELTOR</b> SPORTS MANAGEMENT</span><span class="page__doc">Brand Guideline</span></header>
    <span class="page__label" style="top:27px;">ICON</span>
    <span class="abs tiny" style="left:17px;top:49px;">Option 1:</span>
    <span class="abs tiny" style="left:17px;top:84px;">Option 2:</span>

    <div class="icon-cap" style="left:64px;top:50px;"><svg width="7" height="7" viewBox="0 0 10 10"><circle cx="5" cy="5" r="4.5" fill="none" stroke="#333" stroke-width=".7"/><path d="M3.5 3 L4.5 3 L5 4.3 L4.4 4.8 Q5 6 5.8 6.4 L6.3 5.8 L7.4 6.3 L7.2 7.2 Q4 7.3 3.2 3.6Z" fill="#333"/></svg>Phone icon</div>
    <div class="icon-cap" style="left:113px;top:50px;"><svg width="7" height="7" viewBox="0 0 10 10"><circle cx="5" cy="5" r="4.5" fill="none" stroke="#333" stroke-width=".7"/><circle cx="5" cy="5" r="2.2" fill="none" stroke="#333" stroke-width=".6"/><path d="M2.8 5 H7.2 M5 2.8 V7.2" stroke="#333" stroke-width=".5"/></svg>Website icon</div>
    <div class="icon-cap" style="left:162px;top:50px;"><svg width="7" height="7" viewBox="0 0 10 10"><circle cx="5" cy="5" r="4.5" fill="none" stroke="#333" stroke-width=".7"/><path d="M5 2.4 A1.8 1.8 0 0 1 6.8 4.2 Q6.8 5.4 5 7.6 Q3.2 5.4 3.2 4.2 A1.8 1.8 0 0 1 5 2.4Z" fill="#333"/></svg>Address icon</div>

    <div class="icon-cap" style="left:64px;top:85px;"><svg width="7" height="7" viewBox="0 0 10 10"><circle cx="5" cy="5" r="4.5" fill="none" stroke="#caaa72" stroke-width=".7"/><path d="M3.5 3 L4.5 3 L5 4.3 L4.4 4.8 Q5 6 5.8 6.4 L6.3 5.8 L7.4 6.3 L7.2 7.2 Q4 7.3 3.2 3.6Z" fill="#caaa72"/></svg>Phone icon</div>
    <div class="icon-cap" style="left:113px;top:85px;"><svg width="7" height="7" viewBox="0 0 10 10"><circle cx="5" cy="5" r="4.5" fill="none" stroke="#caaa72" stroke-width=".7"/><circle cx="5" cy="5" r="2.2" fill="none" stroke="#caaa72" stroke-width=".6"/><path d="M2.8 5 H7.2 M5 2.8 V7.2" stroke="#caaa72" stroke-width=".5"/></svg>Website icon</div>
    <div class="icon-cap" style="left:162px;top:85px;"><svg width="7" height="7" viewBox="0 0 10 10"><circle cx="5" cy="5" r="4.5" fill="none" stroke="#caaa72" stroke-width=".7"/><path d="M5 2.4 A1.8 1.8 0 0 1 6.8 4.2 Q6.8 5.4 5 7.6 Q3.2 5.4 3.2 4.2 A1.8 1.8 0 0 1 5 2.4Z" fill="#caaa72"/></svg>Address icon</div>
    <span class="page__num">Page IV</span>
  </section>

</main>
</body>
</html>
```